Website Home Page Graphics / Banner

We need a Website Home page banner or graphic that is engaging and describes what we do with either words or a graphic story- which is Screen Print & Create promotional products. I love the minimalist design style, but I also want the home page to be descriptive and inviting which I feel it is not. Here is a link to our current website www.copperleafprinting.com Our current tagline is
"Here at Copperleaf Press, we take a personal approach to screen-printing. Let us support you in creating a product that leaves a lasting impression."
We are sticking with the Black, White, Grey & Green theme as seen on the website. Attached are some photos that inspire me / I would like to replicate in some way on my own home page.

Target Market(s)

Anybody who needs Promotional Products. Although we can relate most to small Businesses and the younger (age 19-35) demographic

Other font styles liked:
• Heritage, Helvetica Neu - those are my current fonts

Colors
86cfc6
ffffff
c6c6c6
000000
919191

Requirements
Must have
• Engaging Graphic Story that describes in either pictures or words what we do.
Nice to have
• Warm inviting design

```html
<!DOCTYPE html>
<html lang="en">
<head>
<meta charset="utf-8">
<title>Copperleaf Press – Home Banner</title>
<link href="https://fonts.googleapis.com/css2?family=Oswald:wght@500&family=Questrial&display=swap" rel="stylesheet">
<style>
  :root {
    --teal: #56b9b2;
    --ink: #2a2a2a;
    --charcoal: #333333;
    --white: #ffffff;
    --stage: #b3b3b3;
    --garment: #d9d9d9;
    --garment-dark: #c6c6c6;
  }
  html, body {
    margin: 0;
    width: 1200px;
    height: 1200px;
    overflow: hidden;
    background: var(--stage);
  }
  .banner {
    position: absolute;
    left: 0;
    top: 385px;
    width: 1200px;
    height: 431px;
    background: var(--white);
    overflow: hidden;
  }
  .banner__shapes {
    position: absolute;
    inset: 0;
  }
  .brand-name {
    position: absolute;
    left: 40px;
    width: 476px;
    top: 100px;
    text-align: center;
    font-family: "Questrial", sans-serif;
    font-size: 52px;
    color: #111;
    margin: 0;
    letter-spacing: 0.5px;
  }
  .visit-label {
    position: absolute;
    left: 60px;
    width: 392px;
    top: 200px;
    text-align: center;
    font-family: "Oswald", sans-serif;
    font-weight: 500;
    font-size: 68px;
    line-height: 1;
    color: var(--teal);
    margin: 0;
  }
  .web-button {
    position: absolute;
    left: 100px;
    top: 293px;
    width: 300px;
    height: 58px;
    border: 4px solid var(--teal);
    border-radius: 32px;
    background: linear-gradient(#3a3a3a, #111);
    box-shadow: 0 10px 10px -6px rgba(0,0,0,0.35);
    color: var(--white);
    font-family: "Questrial", sans-serif;
    font-size: 18px;
    display: flex;
    align-items: center;
    justify-content: center;
  }
  .tagline {
    position: absolute;
    right: 62px;
    top: 40px;
    margin: 0;
    text-align: right;
    font-family: "Questrial", sans-serif;
    font-size: 26.5px;
    line-height: 33.5px;
    color: var(--ink);
    font-weight: 400;
    -webkit-text-stroke: 0.4px currentColor;
  }
  .tagline__accent { color: var(--teal); }
  .product {
    position: absolute;
    background: linear-gradient(160deg, var(--garment), var(--garment-dark));
    border-radius: 6px;
  }
  .product--tote { left: 592px; top: 240px; width: 114px; height: 138px; }
  .product--sweatshirt { left: 740px; top: 198px; width: 224px; height: 180px; border-radius: 40px 40px 8px 8px; }
  .product--tee { left: 1002px; top: 238px; width: 114px; height: 140px; }
</style>
</head>
<body>
  <section class="banner">
    <svg class="banner__shapes" width="1200" height="431" viewBox="0 0 1200 431" aria-hidden="true">
      <polygon points="0,0 97,0 0,178" fill="var(--teal)"/>
      <polygon points="455,0 583,0 534,152" fill="var(--charcoal)"/>
      <polygon points="583,0 605,0 455,415 447,415" fill="var(--teal)"/>
      <polygon points="1201,230 1201,415 1128,415" fill="var(--teal)"/>
      <rect x="0" y="415" width="1200" height="16" fill="var(--charcoal)"/>
    </svg>

    <h1 class="brand-name">Copperleaf Press</h1>
    <p class="visit-label">VISIT US AT</p>
    <div class="web-button">www.copperleafprinting.com</div>

    <p class="tagline">
      Here at Copperleaf Press, we take a<br>
      <span class="tagline__accent">personal approach to screen-printing</span><br>
      Let us support you in creating a product<br>
      <span class="tagline__accent">that leaves a lasting impression</span>
    </p>

    <div class="product product--tote" role="img" aria-label="Photo of a printed canvas tote bag"></div>
    <div class="product product--sweatshirt" role="img" aria-label="Photo of a grey printed team sweatshirt"></div>
    <div class="product product--tee" role="img" aria-label="Photo of a folded white printed t-shirt"></div>
  </section>
</body>
</html>
```